New Labels for VANTO Sports Drinks

Sports drink company looking for new fresh look with commercial appeal beverage labels. You can use the current label as a guide but adjust where you see fit. Would like to standout from other sports drink on store shelves. VANTO Sports Drinks is a fusion of real brewed tea and all natural electrolytes. Our tea features a bold, full-bodied flavor profile, combined with all natural electrolytes, giving you one of the very first tea based sports drinks.

Target Market(s)

16-40

Colors

Designer to choose colors to be used in the design.

Requirements
Must have
• Name
• flavor
• description
• nutritional info
• all Info on back of labels
Nice to have
• sports image
• fruit flavor
• white background
• Real tea and natural electrolytes
Should not have
• n/a

```html
<!DOCTYPE html>
<html lang="en">
<head>
<meta charset="utf-8">
<title>VANTO Sports Drinks – Label Range</title>
<link href="https://fonts.googleapis.com/css2?family=Archivo+Black&family=Kaushan+Script&family=Cinzel:wght@500&family=Oswald:wght@700&display=swap" rel="stylesheet">
<style>
  :root {
    --page: #ffffff;
    --white: #ffffff;
    --ink: #1c2a22;
    --water-top: #1d4f74;
    --water-mid: #3a7fae;
    --water-low: #ffffff;
    --water-accent: #1ea4f0;
    --water-note: #1976d2;
    --tea-top: #050505;
    --tea-mid: #5a5a5a;
    --tea-low: #ffffff;
    --tea-accent: #e3201b;
    --tea-plus: #e2e2e2;
    --lemon-top: #062b12;
    --lemon-mid: #2f7a14;
    --lemon-low: #c8f51c;
    --lemon-accent: #f4e21a;
    --lemon-tea: #355a1a;
  }
  * { box-sizing: border-box; margin: 0; padding: 0; }
  html, body { width: 1200px; height: 1200px; overflow: hidden; background: var(--page); }
  .canvas { position: relative; width: 1200px; height: 1200px; }

  .label {
    position: absolute;
    width: 375px;
    height: 626px;
    box-shadow: 4px 6px 10px rgba(0,0,0,.45);
    text-align: center;
    overflow: hidden;
    display: flex;
    flex-direction: column;
    align-items: center;
  }
  .label--water { left: 12px;  top: 360px; background: linear-gradient(180deg, var(--water-top) 0%, var(--water-mid) 45%, var(--water-low) 92%); }
  .label--black { left: 412px; top: 207px; background: linear-gradient(180deg, var(--tea-top) 0%, var(--tea-mid) 40%, var(--tea-low) 88%); z-index: 2; }
  .label--lemon { left: 812px; top: 360px; background: linear-gradient(180deg, var(--lemon-top) 0%, var(--lemon-mid) 55%, var(--lemon-low) 100%); }

  .flavor {
    display: block;
    margin-top: 22px;
    font-family: "Oswald", "Arial Narrow", sans-serif;
    font-size: 31px;
    line-height: 1.3;
    letter-spacing: 0.5px;
    color: var(--white);
  }
  .label--lemon .flavor { color: var(--lemon-accent); }

  .brand {
    display: flex;
    justify-content: center;
    align-items: center;
    gap: 12px;
    margin-top: 10px;
    font-family: "Archivo Black", "Arial Black", sans-serif;
    font-size: 66px;
    line-height: 1;
    color: var(--white);
  }
  .brand__mark { width: 32px; height: 32px; }
  .label--water .brand__mark { background: var(--water-accent); }
  .label--black .brand__mark { background: var(--tea-accent); }
  .label--lemon .brand__mark { background: var(--lemon-accent); }

  .product { margin-top: 30px; line-height: 0.9; width: 100%; }
  .product__script {
    display: block;
    font-family: "Kaushan Script", cursive;
    font-size: 58px;
    margin-right: 40px;
    transform: rotate(-8deg);
  }
  .label--water .product__script { color: var(--water-accent); }
  .label--black .product__script { color: var(--tea-accent); }
  .label--lemon .product__script { color: var(--lemon-accent); }
  .product__type {
    display: block;
    margin-top: 6px;
    font-family: "Archivo Black", "Arial Black", sans-serif;
    font-size: 48px;
    color: var(--white);
    margin-left: 90px;
  }

  .art { display: block; margin-top: 14px; width: 300px; border-radius: 40px; flex: none; }
  .art--drop { height: 70px; width: 90px; border-radius: 50% 50% 45% 45%; background: radial-gradient(circle at 45% 40%, rgba(255,255,255,.9), rgba(150,200,230,.5) 70%); }
  .art--minerals { height: 90px; background: linear-gradient(90deg, #c0392b, #8e44ad, #2f80d1, #e67e22, #27ae60); opacity: .85; }
  .art--leaves { height: 170px; background: radial-gradient(ellipse at center, #3f8a2a 0%, #2c6b1e 55%, rgba(44,107,30,0) 75%); }

  .tea {
    display: block;
    margin-top: 6px;
    font-family: "Archivo Black", "Arial Black", sans-serif;
    font-size: 44px;
    line-height: 1;
  }
  .label--black .tea { color: var(--tea-accent); }
  .label--lemon .tea { color: var(--lemon-tea); }
  .plus { width: 48px; height: 48px; display: block; flex: none; margin: 2px auto 0; }
  .label--lemon .plus path { fill: var(--lemon-accent); }
  .label--black .plus path { fill: var(--tea-plus); }

  .infused {
    display: block;
    margin-top: 22px;
    font-family: "Oswald", "Arial Narrow", sans-serif;
    font-size: 24px;
    color: var(--water-note);
  }
  .electrolytes {
    display: block;
    font-family: "Cinzel", Georgia, serif;
    font-size: 34px;
    line-height: 1.2;
    color: var(--ink);
    letter-spacing: -0.5px;
  }
</style>
</head>
<body>
<main class="canvas">

  <section class="label label--water">
    <span class="flavor">POWER WATER</span>
    <div class="brand"><span>VANTO</span><span class="brand__mark"></span></div>
    <div class="product">
      <span class="product__script">Sports</span>
      <span class="product__type">WATER</span>
    </div>
    <div class="art art--drop" role="img" aria-label="Falling water drop illustration"></div>
    <div class="art art--minerals" role="img" aria-label="Cluster of coloured mineral element spheres"></div>
    <span class="infused">INFUSED WITH</span>
    <span class="electrolytes">ELECTROLYTES</span>
  </section>

  <section class="label label--black">
    <span class="flavor">BLACK TEA</span>
    <div class="brand"><span>VANTO</span><span class="brand__mark"></span></div>
    <div class="product">
      <span class="product__script">Sports</span>
      <span class="product__type">TEA</span>
    </div>
    <div class="art art--leaves" role="img" aria-label="Fresh tea leaves over coloured mineral element spheres"></div>
    <span class="tea">TEA</span>
    <svg class="plus" viewBox="0 0 52 52" aria-hidden="true"><path d="M22 4h8v18h18v8H30v18h-8V30H4v-8h18z"/></svg>
    <span class="electrolytes">ELECTROLYTES</span>
  </section>

  <section class="label label--lemon">
    <span class="flavor">LEMON</span>
    <div class="brand"><span>VANTO</span><span class="brand__mark"></span></div>
    <div class="product">
      <span class="product__script">Sports</span>
      <span class="product__type">TEA</span>
    </div>
    <div class="art art--leaves" role="img" aria-label="Fresh tea leaves over coloured mineral element spheres"></div>
    <span class="tea">TEA</span>
    <svg class="plus" viewBox="0 0 52 52" aria-hidden="true"><path d="M22 4h8v18h18v8H30v18h-8V30H4v-8h18z"/></svg>
    <span class="electrolytes">ELECTROLYTES</span>
  </section>

</main>
</body>
</html>
```